Informational Site for Advanced Chemistry R&D

The company develops oxidation chemistry for air, water, fuel pollution controls. The site has been prototyped at www.velkorlabs.net. Take a look. Now, the task is to design it for eye-catching beauty with use of color, on-page scroll-driven color transition and parallax effects. Should capture the themes: high technology, wow it's beautiful, modern, uncluttered, clean urban environment.

Target Market(s)

China Environmentally Conscious Government and Industry,

Industry/Entity Type

It Company

Number of Pages Required

3 page

Font styles to use
Sans Serif

Requirements
Must have
• Parallax effects, desktop compatible, Rich, Modern, Simple, Graphic
Nice to have
• Mobile Phone Compatible
Should not have
• Flash, or anything that is slow to load or requires high bandwidth

```html
<!DOCTYPE html>
<html lang="en">
<head>
<meta charset="utf-8">
<title>VelkorLabs — Advanced Oxidation Science</title>
<link href="https://fonts.googleapis.com/css2?family=Lato:wght@400;700&display=swap" rel="stylesheet">
<style>
:root{
  --teal:#22a6c9;
  --teal-dark:#1b8fb0;
  --blue:#2f8fd8;
  --mint:#bfe8e8;
  --ink:#222;
  --muted:#444;
  --footer:#2b2b2b;
  --white:#fff;
}
*{margin:0;padding:0;box-sizing:border-box}
html,body{width:1200px;height:2439px;overflow:hidden}
body{font-family:'Lato',sans-serif;color:var(--ink);background:var(--white);position:relative}
.abs{position:absolute}

/* top contact tab */
.contact-tab{top:0;left:668px;height:30px;display:flex;font-size:15px;color:var(--white)}
.contact-tab .phone{background:var(--blue);padding:6px 22px 0 28px;clip-path:polygon(14px 0,100% 0,100% 100%,0 100%);display:flex;gap:8px;align-items:flex-start}
.contact-tab .mail{background:var(--teal);padding:7px 28px 0 16px;font-size:13px;clip-path:polygon(0 0,100% 0,calc(100% - 14px) 100%,0 100%);display:flex;gap:8px}

/* header */
.site-header{top:0;left:0;width:1200px;height:102px;background:#f7f7f7}
.brand{left:163px;top:44px;display:flex;align-items:center;gap:12px}
.brand-dot{width:40px;height:40px;border-radius:50%;background:var(--teal)}
.brand-name{font-size:40px;font-weight:700;color:var(--teal)}
.main-nav{left:530px;top:66px;display:flex;align-items:center;font-size:16px;color:#333}
.main-nav a{padding:0 16px;border-left:1px solid #ccc;color:inherit;text-decoration:none}
.main-nav a.home{border:none;padding-left:0}

/* hero */
.hero{top:102px;left:0;width:1200px;height:483px;background:linear-gradient(160deg,#5d6f3d 0%,#3e4a2b 35%,#c0532a 60%,#8b3b22 100%)}
.hero-caption{top:499px;left:0;width:1200px;height:86px;background:rgba(40,150,170,.78);color:var(--white);font-size:26px;text-align:center;padding-top:15px;letter-spacing:.2px}
.hero-dots{top:557px;left:570px;display:flex;gap:8px}
.hero-dots span{width:14px;height:14px;border-radius:50%;background:#ddd}
.hero-dots span.on{background:var(--blue);border:2px solid #ddd}

/* section title */
.sec-title{width:1200px;left:0;text-align:center;font-size:29px;font-weight:400;color:var(--ink)}
.divider{left:0;width:1200px;display:flex;justify-content:center}

/* welcome */
.welcome-title{top:612px}
.welcome-title b{color:var(--teal);font-size:37px;font-weight:700}
.welcome-text{top:708px;left:165px;width:870px;text-align:center;font-size:12.4px;line-height:21px;color:var(--muted)}
.btn{background:var(--blue);color:var(--white);font-size:13px;font-weight:700;text-align:center;border-radius:2px}
.welcome-btn{top:837px;left:551px;width:98px;height:31px;padding-top:8px}

/* services */
.services{top:894px;left:0;width:1200px;height:283px;background:var(--mint)}
.service{top:44px;width:203px}
.service .photo{width:203px;height:148px}
.service h3{margin-top:18px;text-align:center;font-size:16px;font-weight:700;line-height:20px;color:#222}

/* oxidation */
.oxid-left{top:1177px;left:0;width:598px;height:337px;background:radial-gradient(circle at 30% 60%,#3a4148,#252a2f)}
.oxid-right{top:1177px;left:598px;width:602px;height:337px;background:radial-gradient(circle at 50% 50%,#3fb0b0,#1f7f8d 70%,#17607a)}
.oxid-left h2{position:absolute;top:28px;left:0;width:598px;text-align:center;color:var(--white);font-size:27px;font-weight:700}
.oxid-rule{position:absolute;top:80px;left:332px;width:64px;height:4px;background:var(--teal)}
.oxid-left p{position:absolute;top:102px;left:150px;width:428px;text-align:center;color:#ddd;font-size:15px;line-height:25px}
.oxid-list{position:absolute;top:188px;left:205px;list-style:none;color:#ddd;font-size:14.5px}
.oxid-list li{display:flex;align-items:center;gap:16px;margin-bottom:20px}
.oxid-list li::before{content:"";width:8px;height:8px;border-radius:50%;background:var(--teal);box-shadow:0 0 0 3px rgba(34,166,201,.35)}
.oxid-btn{position:absolute;top:276px;left:311px;width:99px;height:32px;padding-top:8px}

/* partners */
.partners-title{top:1540px}
.partner-box{top:1636px;left:161px;width:876px;height:210px;border:1px solid #ddd;border-radius:8px;background:var(--white)}
.partner{position:absolute;top:20px;width:204px;height:190px}
.partner .mark{position:absolute;left:50%;transform:translateX(-50%);top:12px;display:flex;align-items:center;justify-content:center}
.partner .name{font-size:18px;font-weight:700;color:var(--blue);white-space:nowrap}
.partner .label{position:absolute;top:133px;left:0;width:204px;height:41px;background:var(--blue);color:var(--white);font-size:12.5px;text-align:center;line-height:16px;padding-top:5px;border-radius:2px}
.partner .label::before{content:"";position:absolute;top:-7px;left:95px;border:7px solid transparent;border-top:0;border-bottom-color:var(--blue)}
.pager{top:1725px;width:18px;height:18px;border-radius:50%;border:1px solid #bbb;background:var(--white)}

/* testimonials */
.testimonials{top:1865px;left:0;width:1200px;height:300px;background:var(--mint)}
.testi-title{top:1878px}
.avatar{top:1967px;left:171px;width:108px;height:108px;border-radius:50%;border:5px solid var(--teal);background:linear-gradient(135deg,#d9dee2,#a9b4bd)}
.quote{top:1975px;left:318px;width:712px;font-size:12.4px;line-height:21.5px;color:#333;text-indent:30px}
.quote-mark{top:1958px;left:312px;font-size:44px;line-height:1;color:#9aa;font-family:Georgia,serif}
.quote-rule{top:2069px;left:318px;width:710px;height:1px;background:#9dc}
.author{top:2078px;left:318px;font-size:15px;font-weight:700;color:var(--blue)}
.testi-dots{top:2083px;left:997px;display:flex;gap:4px}
.testi-dots span{width:7px;height:7px;border-radius:50%;background:#999}
.testi-dots span.on{background:var(--teal)}

/* footer */
.footer-curve{top:2130px;left:0}
.site-footer{top:2180px;left:0;width:1200px;height:220px;background:var(--footer)}
.foot-col h4{color:var(--white);font-size:15px;font-weight:700;padding-bottom:8px;border-bottom:1px solid #555;width:110px}
.links{list-style:none;margin-top:14px;font-size:11px;color:#ddd;line-height:20.5px}
.links li::before{content:"›";color:#777;margin:0 8px 0 0}
.field{background:var(--white);height:20px;width:190px;margin-top:6px;font-size:10px;color:#666;font-style:italic;padding:3px 6px}
.field.msg{height:36px}
.submit{margin-top:8px;width:54px;height:20px;font-size:11px;padding-top:3px;font-weight:400}
.contact-row{display:flex;gap:10px;font-size:11px;color:#ddd;line-height:16px;margin-top:12px}
.contact-row svg{flex:none;margin-top:2px}
.socials{top:2342px;left:926px;display:flex;gap:8px}
.socials span{width:26px;height:26px;border-radius:50%}
.copyright{top:2400px;left:0;width:1200px;height:39px;background:var(--blue);color:var(--white);font-size:12px;font-weight:700;text-align:center;padding-top:12px}
</style>
</head>
<body>

<header class="site-header abs"></header>
<div class="contact-tab abs">
  <div class="phone">
    <svg width="16" height="16" viewBox="0 0 16 16"><circle cx="8" cy="8" r="7" fill="none" stroke="#fff" stroke-width="1.4"/><path d="M5.5 4.5l1.4 1.2-.7 1.2c.5 1 1.3 1.8 2.3 2.3l1.2-.7 1.2 1.4-1 1c-2.6-.5-4.9-2.8-5.4-5.4z" fill="#fff"/></svg>
    <span>+1 555-014-2290</span>
  </div>
  <div class="mail">
    <svg width="14" height="12" viewBox="0 0 14 12"><rect x="1" y="2" width="12" height="8" fill="none" stroke="#fff"/><path d="M1 2l6 5 6-5" fill="none" stroke="#fff"/></svg>
    <span>info@velkorlabs.net</span>
  </div>
</div>

<div class="brand abs">
  <span class="brand-dot"></span>
  <span class="brand-name">VelkorLabs</span>
</div>

<nav class="main-nav abs">
  <a class="home" href="#" aria-label="Home"><svg width="22" height="20" viewBox="0 0 22 20"><path d="M11 1L1 10h3v9h5v-6h4v6h5v-9h3z" fill="#22a6c9"/></svg></a>
  <a href="#">About Us</a>
  <a href="#">Solutions</a>
  <a href="#">Technology</a>
  <a href="#">Products</a>
  <a href="#">Contact Us</a>
</nav>

<section class="hero abs" role="img" aria-label="Photo of field crew in orange protective suits deploying containment booms along a river bank"></section>
<svg class="abs" style="top:318px;left:98px" width="30" height="50" viewBox="0 0 30 50"><path d="M24 4L6 25l18 21" fill="none" stroke="#fff" stroke-width="2"/></svg>
<svg class="abs" style="top:318px;left:1072px" width="30" height="50" viewBox="0 0 30 50"><path d="M6 4l18 21L6 46" fill="none" stroke="#fff" stroke-width="2"/></svg>
<div class="hero-caption abs">Advanced Oxidation Science for Environmental Pollution Management</div>
<div class="hero-dots abs"><span class="on"></span><span></span><span></span></div>

<h1 class="sec-title welcome-title abs">Welcome to <b>VelkorLabs</b></h1>
<div class="divider abs" style="top:666px">
  <svg width="430" height="26" viewBox="0 0 430 26"><line x1="0" y1="13" x2="200" y2="13" stroke="#bbb"/><line x1="230" y1="13" x2="430" y2="13" stroke="#bbb"/><circle cx="215" cy="13" r="8" fill="none" stroke="#2f8fd8" stroke-width="2"/><circle cx="215" cy="13" r="3" fill="#22a6c9"/></svg>
</div>
<p class="welcome-text abs">Lorem ipsum dolor sit amet, consectetur adipiscing elit. Phasellus nisl metus, bibendum nec ornare commodo, pharetra id quam. Aenean turpis ligula, viverra ut nunc nec, faucibus bibendum augue. Integer turpis urna, euismod at massa nec, varius tincidunt orci. Vivamus lobortis tortor ac neque fringilla viverra. Quisque consectetur neque vitae mauris rutrum ultrices. Vestibulum interdum dapibus ante in convallis. Aliquam auctor purus ut mauris posuere iaculis. Mauris lobortis nulla vitae magna sagittis, malesuada faucibus orci tincidunt. Morbi nisi sem, laoreet ac quam non, feugiat interdum ex. Mauris dignissim lectus sit amet dolor tincidunt, vitae ullamcorper elit mattis. Nulla facilisi.</p>
<a class="btn welcome-btn abs">Read More</a>

<section class="services abs">
  <div class="service abs" style="left:167px"><div class="photo" role="img" aria-label="Photo of a refinery with steel towers and pipework" style="background:linear-gradient(180deg,#9aa3aa,#3c4146)"></div><h3>Fuel Oil<br>Desulfurization</h3></div>
  <div class="service abs" style="left:389px"><div class="photo" role="img" aria-label="Photo of a worker in a respirator handling chemical drums" style="background:linear-gradient(160deg,#c7c3b8,#4b5a70)"></div><h3>Volatile Organic<br>Compounds</h3></div>
  <div class="service abs" style="left:610px"><div class="photo" role="img" aria-label="Photo of industrial smokestacks releasing flue gas" style="background:linear-gradient(180deg,#5a5f6a,#2a2d36)"></div><h3>Flue Gas<br>Scrubbing</h3></div>
  <div class="service abs" style="left:829px"><div class="photo" role="img" aria-label="Photo of a wastewater outfall pouring into a stream" style="background:linear-gradient(160deg,#5d7a3e,#b9a47e)"></div><h3>Wastewater<br>Treatment</h3></div>
</section>

<section class="oxid-left abs">
  <h2>Advanced Oxidation</h2>
  <span class="oxid-rule"></span>
  <p>Advanced Oxidation refers to a variety of techniques employing the Hydroxyl Radical, an energetic, highly reactive cousin of the water molecule :</p>
  <ul class="oxid-list">
    <li>To Add Oxygen To Inorganic Molecules</li>
    <li>To Remove Hydrogen From Organic Molecules</li>
  </ul>
  <a class="btn oxid-btn">Learn More</a>
</section>
<div class="oxid-right abs" role="img" aria-label="Illustration of hydroxyl radical reaction pathways with molecules in yellow circles on a teal background"></div>

<h2 class="sec-title partners-title abs">Our Partners</h2>
<div class="divider abs" style="top:1590px">
  <svg width="320" height="26" viewBox="0 0 320 26"><line x1="0" y1="13" x2="145" y2="13" stroke="#bbb"/><line x1="175" y1="13" x2="320" y2="13" stroke="#bbb"/><circle cx="160" cy="13" r="8" fill="none" stroke="#2f8fd8" stroke-width="2"/><circle cx="160" cy="13" r="3" fill="#22a6c9"/></svg>
</div>
<div class="partner-box abs">
  <div class="partner" style="left:14px"><div class="mark" style="top:60px"><span class="name">Norvane Systems</span></div><div class="label">Our Sales Partner<br>In China</div></div>
  <div class="partner" style="left:229px"><div class="mark" style="top:60px"><span class="name">Castrel</span></div><div class="label">Our Construction Partner<br>In China</div></div>
  <div class="partner" style="left:444px"><div class="mark"><span style="width:108px;height:108px;border-radius:50%;background:#1f5da8;display:block"></span></div><div class="label">Our Technology Partner<br>In China</div></div>
  <div class="partner" style="left:658px"><div class="mark"><span style="width:108px;height:108px;border-radius:50%;background:#b02a30;display:block"></span></div><div class="label">Our Technology Partner<br>In China</div></div>
</div>
<span class="pager abs" style="left:146px"></span>
<span class="pager abs" style="left:1034px"></span>
<svg class="abs" style="top:1730px;left:151px" width="8" height="8" viewBox="0 0 8 8"><path d="M6 0L1 4l5 4z" fill="#333"/></svg>
<svg class="abs" style="top:1730px;left:1040px" width="8" height="8" viewBox="0 0 8 8"><path d="M2 0l5 4-5 4z" fill="#333"/></svg>

<section class="testimonials abs"></section>
<h2 class="sec-title testi-title abs">Client Testimonials</h2>
<div class="divider abs" style="top:1926px">
  <svg width="320" height="26" viewBox="0 0 320 26"><line x1="0" y1="13" x2="145" y2="13" stroke="#999"/><line x1="175" y1="13" x2="320" y2="13" stroke="#999"/><circle cx="160" cy="13" r="8" fill="none" stroke="#2f8fd8" stroke-width="2"/><circle cx="160" cy="13" r="3" fill="#22a6c9"/></svg>
</div>
<div class="avatar abs" role="img" aria-label="Portrait photo of the client"></div>
<svg class="abs" style="top:2068px;left:226px" width="26" height="16" viewBox="0 0 26 16"><path d="M0 0h26L10 16z" fill="#22a6c9"/></svg>
<span class="quote-mark abs">“</span>
<p class="quote abs">Lorem ipsum dolor smit amet, consectetuer adipiscing elitmk, sed amet diam nonummy nibh euismod tincidun nt ut laoreetml dolore magna aliquam erat volutpat. Ut wisi enim ad minim veniam, quis nostrud exer tationk ullamcorper suscipit lobortisk nisl utml aliqpi ex ea commodo consequat. Duis autem vel eumk iriure dolor inj hendrerit inn vulputate velit esse molestiemo consequat, velhki illumn gnol dolore eu feugiat nulla facilisis .</p>
<span class="quote-rule abs"></span>
<span class="author abs">- Mr. John Doe</span>
<div class="testi-dots abs"><span class="on"></span><span></span><span></span></div>

<svg class="footer-curve abs" width="1200" height="60" viewBox="0 0 1200 60">
  <path d="M0 60Q600-40 1200 60z" fill="#2b2b2b"/>
  <path d="M0 52Q600-44 1200 52" fill="none" stroke="#22a6c9" stroke-width="6"/>
</svg>
<footer class="site-footer abs">
  <div class="foot-col abs" style="left:163px;top:36px">
    <h4>Quick Links</h4>
    <ul class="links"><li>Home</li><li>About Us</li><li>Solutions</li><li>Technology</li><li>Products</li><li>Contact Us</li></ul>
  </div>
  <div class="foot-col abs" style="left:363px;top:36px">
    <h4 style="width:190px">Quick Inquiry</h4>
    <div class="field" style="margin-top:14px">Name</div>
    <div class="field">Email</div>
    <div class="field msg">Message</div>
    <div class="btn submit">Submit</div>
  </div>
  <div class="abs" style="left:603px;top:36px;width:1px;height:160px;background:#444"></div>
  <div class="foot-col abs" style="left:649px;top:36px">
    <h4 style="width:200px">Contact Details</h4>
    <div class="contact-row"><svg width="10" height="13" viewBox="0 0 10 13"><path d="M5 0a5 5 0 0 0-5 5c0 4 5 8 5 8s5-4 5-8a5 5 0 0 0-5-5z" fill="#2f8fd8"/><circle cx="5" cy="5" r="2" fill="#2b2b2b"/></svg><span>Velkor Labs Corporation<br>Ashford Bay,<br>U.S.A.</span></div>
    <div class="contact-row" style="margin-top:16px"><svg width="11" height="11" viewBox="0 0 11 11"><path d="M1 1l3 0 1 3-1.5 1c.7 1.3 1.2 1.8 2.5 2.5l1-1.5 3 1v3C5 10 1 6 1 1z" fill="#2f8fd8"/></svg><span>+1 555-014-2290</span></div>
    <div class="contact-row" style="margin-top:18px"><svg width="11" height="9" viewBox="0 0 11 9"><rect x=".5" y=".5" width="10" height="8" fill="#2f8fd8"/><path d="M.5.5l5 4 5-4" fill="none" stroke="#2b2b2b"/></svg><span>info@velkorlabs.net</span></div>
  </div>
</footer>
<div class="socials abs"><span style="background:#3b5998"></span><span style="background:#1da1f2"></span><span style="background:#d6312c"></span></div>
<div class="copyright abs">Copyright © 2016 Velkor Labs .&nbsp; All Right Reserved.</div>

</body>
</html>
```